Label for Skincare Brand

"Fernbrook Organics" - organic skincare brand
I need a label designed for my organic skincare brand. I have attached pics of brands I like, to give you an idea of style. I would like something minimal although some colour might work. Colours I like are pale blush pink and aqua. I would like a clean, minimalistic modern yet elegant label. Please look at the samples because they demonstrate the style I look for in a label. It is okay to add a graphical element into the design as long as it enhances or add value to the design.
We do not have a logo yet, so I'd appreciate if you could create a simple type logo for Fernbrook Organics similar to the examples attached.
Please can you do two different sizes: one cream jar and one serum bottle. Both will contain the same information.
___________________________________________________
1. Cream Jar (label size 42 x 190 mm) (clear glass with aluminium lid)
2. Serum Bottle (label size 50 x 110 mm) (clear glass with black pump)
FRONT SIDE:
Fernbrook Organics
Moonpetal
Ultimate Anti-Aging Cream
For Dry & Mature Skin
Organic & Palm Oil-Free
100 ml.
BACK SIDE:
Moonpetal Radiance Renewal Cream
An effective Day Cream that harnesses the best of science to target the signs of aging. The main active ingredient is K7M, a patented noncomedogenic lipid complex, carefully engineered from botanically-sourced lipids. It is composed of a variety of lipid types which are carefully combined in the same ratio as those found on healthy young skin of an average 22 year old.
Directions:
Apply to clean skin morning and night.
Ingredients:
Aloe Vera Leaf Juice, Cocos Nucifera Oil, Butyrospermum Parkii Butter, Jojoba Oil/Macadamia Seed Oil Esters (and) Squalene (and) Phytosteryl Macadamiate (and) Phytosterols, Potassium Olivoyl Hydrolyzed Oat Protein (and) Cetearyl Alcohol (and) Glyceryl Oleate (and) Glyceryl Stearat, Benzyl Alcohol, Dehydroacetic Acid.
Fernbrook Organics
3/6 Kellerton Parade West, Marlowe Heights, NSW 2999
www.fernbrookorganics.example
Any questions, please just ask away. Thank you.

```html
<!DOCTYPE html>
<html lang="en">
<head>
<meta charset="utf-8">
<title>Fernbrook Organics – Moonpetal Labels</title>
<link rel="stylesheet" href="https://fonts.googleapis.com/css2?family=Montserrat:wght@400;500&family=Inter:wght@400&display=swap">
<style>
  :root{
    --bg:#efeff1;
    --paper:#ffffff;
    --ink:#1e1e1e;
    --grey:#555;
    --blush:#f3d5d5;
    --blush-text:#e7a8a8;
    --rule:#eec2c2;
  }
  *{box-sizing:border-box;margin:0;padding:0}
  html,body{width:1200px;height:849px;overflow:hidden}
  body{background:var(--bg);position:relative;font-family:"Inter",sans-serif;color:var(--ink)}
  .label{position:absolute;background:var(--paper);box-shadow:0 1px 3px rgba(0,0,0,.08)}

  /* wordmark: invented name in the piece's own text font, one colour, one weight */
  .wordmark{font-family:"Montserrat",sans-serif;font-weight:500;font-size:13px;letter-spacing:.14em;color:var(--ink);white-space:nowrap}

  .product-name{font-family:"Montserrat",sans-serif;font-weight:500;letter-spacing:.32em;text-transform:uppercase;font-size:17px}
  .product-sub{font-family:"Inter",sans-serif;font-size:13px;color:var(--grey);margin-top:3px}
  .skin-type{font-family:"Montserrat",sans-serif;font-size:9.5px;letter-spacing:.22em;text-transform:uppercase;color:var(--grey);margin-top:18px}
  .claim{display:flex;align-items:center;gap:6px;font-family:"Montserrat",sans-serif;font-size:9px;letter-spacing:.12em;color:var(--grey);margin-top:8px}
  .claim svg{width:11px;height:11px;flex:none}
  .rule{height:1.5px;background:var(--rule)}
  .volume{width:56px;height:56px;border-radius:50%;background:var(--blush);display:flex;align-items:center;justify-content:center;font-family:"Montserrat",sans-serif;font-size:9.5px;letter-spacing:.12em;color:var(--grey)}

  /* jar wrap strip */
  .jar-strip{left:40px;top:60px;width:540px;height:120px;display:flex;align-items:center;padding:0 34px;gap:26px}
  .jar-strip__divider{width:1.5px;height:64px;background:var(--rule)}
  .jar-strip .product-name{font-size:19px}

  /* box back panel */
  .box-back{left:40px;top:225px;width:260px;height:560px;padding:26px 22px;border-top:22px solid var(--blush)}
  .box-back__title{font-family:"Montserrat",sans-serif;font-weight:500;font-size:15px;letter-spacing:.3em;text-transform:uppercase;color:var(--blush-text)}
  .box-back__sub{font-size:10px;color:var(--blush-text);margin:2px 0 14px}
  .box-back p{font-size:8.6px;line-height:1.5;color:var(--grey);margin-bottom:9px}
  .box-back .heading{margin-bottom:0;color:var(--ink)}
  .box-back__web{font-family:"Montserrat",sans-serif;font-size:8px;letter-spacing:.14em;text-transform:uppercase;color:var(--blush-text);margin-top:6px}

  /* box front panel */
  .box-front{left:320px;top:225px;width:260px;height:560px;border-top:22px solid var(--blush);padding:64px 26px 0;display:flex;flex-direction:column;align-items:center;text-align:center}
  .box-front .rule{width:150px;margin:26px 0 28px}
  .box-front .volume{margin-top:auto;margin-bottom:40px}

  /* serum bottle label */
  .bottle-label{left:780px;top:170px;width:300px;height:500px;padding:74px 30px 0;display:flex;flex-direction:column;align-items:center;text-align:center}
  .bottle-label .rule{width:220px;margin:26px 0 28px}
  .bottle-label .volume{margin-top:auto;margin-bottom:50px;width:62px;height:62px}
</style>
</head>
<body>

  <!-- cream jar wrap label -->
  <section class="label jar-strip">
    <span class="wordmark">Fernbrook Organics</span>
    <span class="jar-strip__divider"></span>
    <div>
      <h1 class="product-name">Moonpetal</h1>
      <p class="product-sub">Ultimate Anti-Aging Cream</p>
    </div>
  </section>

  <!-- box back panel -->
  <section class="label box-back">
    <h2 class="box-back__title">Moonpetal</h2>
    <p class="box-back__sub">Radiance Renewal Cream</p>
    <p>An effective Day Cream that harnesses the best of science to target the signs of aging. The main active ingredient is K7M, a patented noncomedogenic lipid complex, carefully engineered from botanically-sourced lipids. It is composed of a variety of lipid types which are carefully combined in the same ratio as those found on healthy young skin of an average 22 year old.</p>
    <p class="heading">Directions:</p>
    <p>Apply to clean skin morning and night.</p>
    <p class="heading">Ingredients:</p>
    <p>Aloe Vera Leaf Juice, Cocos Nucifera Oil, Butyrospermum Parkii Butter, Jojoba Oil/Macadamia Seed Oil Esters (and) Squalene (and) Phytosteryl Macadamiate (and) Phytosterols, Potassium Olivoyl Hydrolyzed Oat Protein (and) Cetearyl Alcohol (and) Glyceryl Oleate (and) Glyceryl Stearat, Benzyl Alcohol, Dehydroacetic Acid.</p>
    <p>Fernbrook Organics<br>3/6 Kellerton Parade West, Marlowe Heights, NSW 2999</p>
    <div class="box-back__web">www.fernbrookorganics.example</div>
  </section>

  <!-- box front panel -->
  <section class="label box-front">
    <span class="wordmark">Fernbrook Organics</span>
    <div class="rule"></div>
    <h2 class="product-name">Moonpetal</h2>
    <p class="product-sub">Ultimate Anti-Aging Cream</p>
    <p class="skin-type">For Dry &amp; Mature Skin</p>
    <p class="claim">
      <svg viewBox="0 0 12 12" aria-hidden="true"><circle cx="6" cy="6" r="6" fill="#1e1e1e"/><path d="M3.4 6.2l1.8 1.7 3.4-3.6" stroke="#fff" stroke-width="1.3" fill="none"/></svg>
      Organic &amp; Palm Oil-Free
    </p>
    <div class="volume">100 ml.</div>
  </section>

  <!-- serum bottle label -->
  <section class="label bottle-label">
    <span class="wordmark">Fernbrook Organics</span>
    <div class="rule"></div>
    <h2 class="product-name">Moonpetal</h2>
    <p class="product-sub">Ultimate Anti-Aging Cream</p>
    <p class="skin-type">For Dry &amp; Mature Skin</p>
    <p class="claim">
      <svg viewBox="0 0 12 12" aria-hidden="true"><circle cx="6" cy="6" r="6" fill="#1e1e1e"/><path d="M3.4 6.2l1.8 1.7 3.4-3.6" stroke="#fff" stroke-width="1.3" fill="none"/></svg>
      Organic &amp; Palm Oil-Free
    </p>
    <div class="volume">100 ml.</div>
  </section>

</body>
</html>
```